Marlow Estate Group (Real Estate and Investment)

A high end, clean design.
We are a real estate company with sales, asset management and investment divisions. We want to use a black and white scheme which is really high end feel. The back of the card can just be the logo (black background with the white writing) as we will probably emboss this when we print)

Target Market(s)

High level investors, high end houses for sale

Industry/Entity Type

Business

Contact Information for Business Card

Name, position, phone number and email address
Ben Marlow, Managing Director, 0438926057 and ben@marlowestate.com.au

Requirements
Must have
• Back of the card to be the black background with the white writing (as per the attached images). Would like the capacity to emboss the writing and logo

```html
<!DOCTYPE html>
<html lang="en">
<head>
<meta charset="utf-8">
<title>Marlow Estate Group – Business Card</title>
<link href="https://fonts.googleapis.com/css2?family=Open+Sans:wght@400;700&display=swap" rel="stylesheet">
<style>
  :root {
    --stage: #e9e7e4;
    --card-black: #111111;
    --emboss: #2c2c2c;
    --card-white: #ffffff;
    --ink: #1a1a1a;
    --ink-soft: #3a3a3a;
    --rule: #222222;
  }
  html, body {
    margin: 0;
    padding: 0;
    width: 1200px;
    height: 1200px;
    overflow: hidden;
    background: var(--stage);
    font-family: "Open Sans", sans-serif;
  }
  .canvas {
    width: 1200px;
    height: 1200px;
    display: flex;
    flex-direction: column;
    align-items: center;
    justify-content: center;
    gap: 70px;
  }
  .card {
    width: 770px;
    height: 440px;
    position: relative;
    box-shadow: 0 10px 30px rgba(0,0,0,0.18);
    box-sizing: border-box;
  }
  /* Back of card */
  .card--back {
    background: var(--card-black);
    display: flex;
    flex-direction: column;
    align-items: center;
    justify-content: center;
    gap: 26px;
  }
  .brand-dot {
    width: 110px;
    height: 110px;
    border-radius: 50%;
    border: 2px solid var(--emboss);
  }
  .brand-name {
    color: var(--emboss);
    font-weight: 700;
    font-size: 34px;
    letter-spacing: 1px;
    text-transform: uppercase;
  }
  /* Front of card */
  .card--front {
    background: var(--card-white);
    padding: 0 44px;
  }
  .rule {
    position: absolute;
    left: 44px;
    right: 44px;
    height: 2px;
    background: var(--rule);
  }
  .rule--top { top: 150px; }
  .rule--bottom { top: 318px; }
  .contact {
    position: absolute;
    display: flex;
    align-items: center;
    gap: 8px;
    font-size: 17px;
    color: var(--ink-soft);
  }
  .contact svg { width: 15px; height: 15px; fill: var(--ink); }
  .contact--phone { left: 44px; top: 166px; }
  .contact--email { left: 230px; top: 262px; }
  .contact--web { right: 44px; top: 262px; }
  .identity {
    position: absolute;
    left: 0;
    right: 0;
    top: 196px;
    text-align: center;
  }
  .identity__name {
    margin: 0;
    font-weight: 700;
    font-size: 25px;
    color: var(--ink);
    text-transform: uppercase;
    line-height: 1.1;
  }
  .identity__role {
    margin: 2px 0 0;
    font-size: 17px;
    color: var(--ink-soft);
  }
</style>
</head>
<body>
<main class="canvas">
  <section class="card card--back" aria-label="Card back">
    <div class="brand-dot"></div>
    <div class="brand-name">Marlow Estate Group</div>
  </section>

  <section class="card card--front" aria-label="Card front">
    <div class="rule rule--top"></div>

    <div class="contact contact--phone">
      <svg viewBox="0 0 24 24" aria-hidden="true"><path d="M6.6 10.8a15.1 15.1 0 0 0 6.6 6.6l2.2-2.2a1 1 0 0 1 1-.25 11.4 11.4 0 0 0 3.6.57 1 1 0 0 1 1 1V20a1 1 0 0 1-1 1A17 17 0 0 1 3 4a1 1 0 0 1 1-1h3.5a1 1 0 0 1 1 1c0 1.25.2 2.45.57 3.57a1 1 0 0 1-.25 1z"/></svg>
      <span>0438926057</span>
    </div>

    <div class="identity">
      <h1 class="identity__name">Ben Marlow</h1>
      <p class="identity__role">Managing Director</p>
    </div>

    <div class="contact contact--email">
      <svg viewBox="0 0 24 24" aria-hidden="true"><path d="M2 5h20v14H2z M3 6.5v.4l9 6 9-6v-.4z" fill-rule="evenodd"/></svg>
      <span>ben@marlowestate.com.au</span>
    </div>

    <div class="contact contact--web">
      <svg viewBox="0 0 24 24" aria-hidden="true"><path d="M12 2a10 10 0 1 0 0 20 10 10 0 0 0 0-20zm0 2c.9 1.2 1.6 2.6 2 4h-4c.4-1.4 1.1-2.8 2-4zM4.3 14a8 8 0 0 1 0-4h3.4a16 16 0 0 0 0 4zm.8 2h3c.3 1.3.8 2.5 1.4 3.6A8 8 0 0 1 5.1 16zm3-8h-3a8 8 0 0 1 4.4-3.6C8.9 5.5 8.4 6.7 8.1 8zM12 20c-.9-1.2-1.6-2.6-2-4h4c-.4 1.4-1.1 2.8-2 4zm2.3-6H9.7a14 14 0 0 1 0-4h4.6a14 14 0 0 1 0 4zm.2 5.6c.6-1.1 1.1-2.3 1.4-3.6h3a8 8 0 0 1-4.4 3.6zM16.3 14a16 16 0 0 0 0-4h3.4a8 8 0 0 1 0 4zm-.4-6c-.3-1.3-.8-2.5-1.4-3.6A8 8 0 0 1 18.9 8z"/></svg>
      <span>www.marlowestate.com.au</span>
    </div>

    <div class="rule rule--bottom"></div>
  </section>
</main>
</body>
</html>
```